USB Stick Gewinnspiel
Zielgruppe
Männer, Technikinteressierte
Aufgabenstellung
Design für ein Gewinnspiel bei dem es 100 USB Sticks, 32 GB (mit die kleinsten USB Sticks der Welt) zu gewinnen gibt.
Menüpunkte: Startseite, Teilnahmebedingungen, Preisdetails, Teilnehmen, Datenschutz.
Es soll eine Intro-Seite auf der der Preis groß heraus gestellt ist gestaltet werden mit den entsprechenden Menüpunkten sowie eine Template-Seite in der wir dann alle notwendigen Inhalte einfügen können. Von der Gestaltung her seid Ihr frei. Klein ist jedoch sexy, daher darf der USB Stick mit einer sexy Dame präsentiert werden die Männerherzen höher schlagen läßt.
Gewinnspiele von uns finden Sie auf www.glueckspfad.de damit Sie sich ein Bild über die bisherigen Gewinnspiele machen können.
WICHTIG: Es soll nur die Eingangsseite und eine Template Seite erstellt werden. Die komplette Programmierung bzw. Füllung mit Inhalten wird von uns gemacht! Für die Templateseite wäre eine Breite von 500 Pixeln oder mehr im Bereich wo wir Inhalte einfügen können wünschenswert.
„Normales altbackenes“ HTML mit Tabellen ohne großen CSS Schnick-Schnack würden wir bevorzugen da es für uns einfacher zum Bearbeiten ist.
Das Gewinnspiel wird später auf einer Subdomain laufen und hat somit keinen Domainnamen den man im Titel darstellen kann oder muss.
Das fertige Layout soll dann als geschnittene HTML Datei mit verlinkten Grafiken geliefert werden.

```html
<!DOCTYPE html>
<html lang="de">
<head>
<meta charset="utf-8">
<title>Jetzt hier gewinnen – USB Stick Gewinnspiel</title>
<link rel="stylesheet" href="https://fonts.googleapis.com/css2?family=Black+Ops+One&family=Arimo:wght@400;700&display=swap">
<style>
  :root {
    --page-grey: #a4a4a4;
    --menu-text: #ffffff;
    --panel-white: #ffffff;
    --info-dark: #24262a;
    --info-text: #f2f2f2;
    --accent-red: #c8141c;
    --accent-red-dark: #8e0c12;
    --headline-fill: #f4f4f4;
    --headline-edge: #3a3a3a;
    --photo-light: #e4e2e0;
    --photo-mid: #9b948f;
    --product-light: #f7f7f7;
    --product-dark: #2a2a2a;
  }
  * { box-sizing: border-box; margin: 0; padding: 0; }
  html, body { width: 1200px; height: 900px; overflow: hidden; }
  body {
    background: var(--page-grey);
    font-family: "Arimo", Arial, sans-serif;
    position: relative;
  }
  .main-menu {
    position: absolute; top: 48px; left: 0; width: 1200px;
    text-align: center; color: var(--menu-text); font-size: 20px;
  }
  .main-menu a { color: var(--menu-text); text-decoration: none; }
  .main-menu .divider { margin: 0 16px; }
  .headline {
    position: absolute; top: 118px; left: 195px; width: 803px;
    font-family: "Black Ops One", "Arial Black", sans-serif;
    font-size: 66px; line-height: 1; letter-spacing: 3px;
    color: var(--headline-fill); text-align: center; white-space: nowrap;
    text-shadow: 0 0 2px var(--headline-edge), 2px 2px 0 var(--headline-edge);
  }
  .prize-panel {
    position: absolute; top: 183px; left: 195px; width: 803px; height: 525px;
    background: var(--panel-white);
    box-shadow: 0 4px 14px rgba(0,0,0,0.35);
  }
  .hero-photo {
    position: absolute; left: 12px; top: 15px; width: 344px; height: 498px;
    background: linear-gradient(160deg, var(--photo-light) 0%, #cfcac6 45%, var(--photo-mid) 100%);
  }
  .info-box {
    position: absolute; left: 368px; top: 15px; width: 420px; height: 243px;
    background: var(--info-dark); color: var(--info-text);
  }
  .product-name {
    position: absolute; left: 42px; top: 160px;
    font-size: 22px; font-weight: 700; color: var(--info-text);
  }
  .product-sub {
    position: absolute; left: 42px; top: 190px; font-size: 13px;
  }
  .feature-list {
    position: absolute; left: 168px; top: 36px; width: 245px;
    list-style: none; font-size: 13.5px; line-height: 19.5px;
  }
  .feature-list li { padding-left: 14px; text-indent: -14px; }
  .feature-list li::before { content: "-\00a0\00a0"; }
  .product-photo {
    position: absolute; left: 368px; top: 270px; width: 420px; height: 110px;
    background: radial-gradient(ellipse at 55% 50%, #8d8d8d 0%, #d8d8d8 40%, var(--product-light) 70%);
  }
  .join-button {
    position: absolute; left: 368px; top: 389px; width: 420px; height: 124px;
    background: linear-gradient(180deg, #7a1015 0%, var(--accent-red) 35%, var(--accent-red-dark) 100%);
    color: #ffffff; text-decoration: none;
    font-family: "Black Ops One", "Arial Black", sans-serif;
  }
  .join-button .small { position: absolute; left: 66px; top: 26px; font-size: 19px; }
  .join-button .big { position: absolute; left: 44px; top: 40px; font-size: 52px; letter-spacing: 1px; }
  .odds-badge {
    position: absolute; left: 540px; top: 168px; width: 140px; height: 165px;
  }
</style>
</head>
<body>
  <nav class="main-menu">
    <a href="#">Startseite</a><span class="divider">|</span><a href="#">Preisdetails</a><span class="divider">|</span><a href="#">Datenschutz</a><span class="divider">|</span><a href="#">Teilnahmebedingungen</a><span class="divider">|</span><a href="#">Impressum</a>
  </nav>

  <h1 class="headline">JETZT HIER GEWINNEN</h1>

  <section class="prize-panel">
    <div class="hero-photo" role="img" aria-label="Foto: lachende Frau zeigt auf einen Laptop mit dem winzigen 32 GB USB-Stick"></div>

    <div class="info-box">
      <ul class="feature-list">
        <li>32 GB Speicherkapazität!</li>
        <li>Winziger USB-Speicherstick</li>
        <li>Befestigung am Schlüsselbund</li>
        <li>Superschneller Datentransfer über USB2.0-Schnittstelle</li>
        <li>Staub- und wasserdichter Korpus aus leichtem Kunststoff</li>
        <li>Mit der kleinste USB-Stick der Welt!</li>
        <li>21 x 16 x 16 mm, 2 g</li>
      </ul>
      <div class="product-name">Tinyport</div>
      <div class="product-sub">USB Sticks</div>
    </div>

    <div class="product-photo" role="img" aria-label="Produktfoto: schwarzer Mini-USB-Stick mit Kappe und Schlüsselband"></div>

    <a class="join-button" href="#">
      <span class="small">KOSTENLOS</span>
      <span class="big">TEILNEHMEN</span>
    </a>
  </section>

  <svg class="odds-badge" viewBox="0 0 140 165" aria-label="1 von 100">
    <path d="M28 12 Q38 4 50 10 L128 60 Q138 68 128 78 L40 158 Q28 166 22 152 L6 40 Q4 24 28 12 Z" fill="#c8141c" stroke="#ffffff" stroke-width="2"/>
    <text x="46" y="52" fill="#ffffff" font-family="Arimo, Arial, sans-serif" font-size="15" font-weight="700" text-anchor="middle">1</text>
    <text x="46" y="68" fill="#ffffff" font-family="Arimo, Arial, sans-serif" font-size="15" font-weight="700" text-anchor="middle">VON</text>
    <text x="52" y="112" fill="#ffffff" font-family="Arimo, Arial, sans-serif" font-size="46" font-weight="700" text-anchor="middle">100</text>
  </svg>
</body>
</html>
```